Ayurvedic Beauty Company in Need of Business Cards

My company is a high-end ayurvedic beauty brand. I need a business card that represents that. The designer should utilize logo and color palette. I want these cards to be printed with the foil accents so keep that in mind.

I have attached the ai of my logo and business card info. As well as, some of the product we are launching soon, they do not have to be on the card.

Be creative and have fun.

Thanks in advance,

Marla

```html
<!DOCTYPE html>
<html lang="en">
<head>
<meta charset="utf-8">
<title>Amber Lotus – Business Card</title>
<link href="https://fonts.googleapis.com/css2?family=Open+Sans:wght@400;600&display=swap" rel="stylesheet">
<style>
  :root {
    --page-bg: #efece6;
    --card-black: #111111;
    --card-white: #ffffff;
    --foil-gold: #c6a87c;
    --foil-gold-deep: #a88a5e;
    --ink-dark: #2b2b2b;
  }
  * { margin: 0; padding: 0; box-sizing: border-box; }
  html, body {
    width: 1200px;
    height: 900px;
    overflow: hidden;
    background: var(--page-bg);
    font-family: "Open Sans", Arial, sans-serif;
  }
  .card-sheet {
    width: 1200px;
    height: 900px;
    display: flex;
    align-items: center;
    justify-content: center;
    gap: 40px;
  }
  .card {
    position: relative;
    width: 540px;
    height: 309px;
    overflow: hidden;
    box-shadow: 0 6px 18px rgba(0,0,0,0.18);
  }

  /* Front */
  .card-front {
    background: var(--card-black);
    display: flex;
    flex-direction: column;
    align-items: center;
    justify-content: center;
    gap: 22px;
  }
  .brand-dot {
    width: 74px;
    height: 74px;
    border-radius: 50%;
    background: var(--foil-gold);
  }
  .brand-name {
    color: var(--foil-gold);
    font-weight: 600;
    font-size: 21px;
    letter-spacing: 1px;
  }

  /* Back */
  .card-back { background: var(--card-white); }
  .card-wave {
    position: absolute;
    inset: 0;
    width: 100%;
    height: 100%;
  }
  .holder {
    position: absolute;
    left: 34px;
    top: 58px;
  }
  .holder-name {
    color: var(--foil-gold);
    font-weight: 600;
    font-size: 19px;
    letter-spacing: 0.5px;
    line-height: 1.2;
  }
  .holder-title {
    color: var(--ink-dark);
    font-size: 15px;
    line-height: 1.3;
  }
  .back-brand {
    position: absolute;
    right: 36px;
    top: 56px;
    display: flex;
    align-items: center;
    gap: 12px;
  }
  .back-brand .brand-dot { width: 40px; height: 40px; }
  .back-brand .brand-name { font-size: 18px; }
  .contact-list {
    position: absolute;
    left: 58px;
    top: 158px;
    list-style: none;
  }
  .contact-item {
    display: flex;
    align-items: center;
    gap: 9px;
    color: var(--ink-dark);
    font-size: 14.5px;
    line-height: 19px;
  }
  .contact-icon {
    width: 11px;
    height: 11px;
    fill: var(--foil-gold-deep);
    flex: none;
  }
</style>
</head>
<body>
<main class="card-sheet">

  <section class="card card-front" aria-label="Card front">
    <span class="brand-dot"></span>
    <span class="brand-name">AMBER LOTUS</span>
  </section>

  <section class="card card-back" aria-label="Card back">
    <svg class="card-wave" viewBox="0 0 540 309" preserveAspectRatio="none" aria-hidden="true">
      <path d="M0 280 C200 276 310 252 395 192 C445 158 495 142 540 138 L540 309 L0 309 Z" fill="var(--foil-gold)"/>
      <path d="M0 287 C200 283 312 259 398 199 C448 165 497 149 540 145 L540 309 L0 309 Z" fill="var(--card-white)"/>
      <path d="M0 292 C200 288 314 264 400 204 C450 170 498 154 540 150 L540 309 L0 309 Z" fill="var(--card-black)"/>
    </svg>

    <div class="holder">
      <div class="holder-name">MARLA VANCE</div>
      <div class="holder-title">CEO</div>
    </div>

    <div class="back-brand">
      <span class="brand-dot"></span>
      <span class="brand-name">AMBER LOTUS</span>
    </div>

    <ul class="contact-list">
      <li class="contact-item">
        <svg class="contact-icon" viewBox="0 0 12 12"><path d="M1 3 Q1 1 3 1 H9 Q11 1 11 3 V4 H8 V3 H4 V4 H1 Z M3 5 H9 L11 11 H1 Z"/></svg>
        1(888) 555-0142
      </li>
      <li class="contact-item">
        <svg class="contact-icon" viewBox="0 0 12 12"><path d="M3 0 H9 V12 H3 Z M4 1.5 V9.5 H8 V1.5 Z"/></svg>
        1(347) 555-0187
      </li>
      <li class="contact-item">
        <svg class="contact-icon" viewBox="0 0 12 12"><path d="M0 2 H12 V10 H0 Z M1 3 L6 7 L11 3 Z"/></svg>
        marla@loveamberlotus.com
      </li>
      <li class="contact-item">
        <svg class="contact-icon" viewBox="0 0 12 12"><circle cx="6" cy="6" r="6"/></svg>
        www.loveamberlotus.com
      </li>
    </ul>
  </section>

</main>
</body>
</html>
```